Circular Wedding Menu Design - Adobe Illustrator

I am looking for a design for circular wedding menus. these will be 7 inches.I'm providing a template from the printer, AI files of our wedding invitation, and the menu items.

The paper our invitations were printed on was a sandy beige color. please make the background for this the same color. It will be put ontop of a white plate with ivory tablecloth and cappucino covered napkins.

IMPORTANT - We aren't committed to a specific design so feel free to use whatever you like, but we definitely want the cow, fish, and carrot images from our rsvp to be used for the entrees in the menu.

IMPORTANT - must be in Adobe illustrator format

for inspiration:
http://cdn.velvorabridalnotes.example/wp-content/uploads/2012/10/tormane-styled-19.jpg

http://www.quorbelsearch.example/imgres?imgurl=http%3A%2F%2Fwww.dellivanestudio.example%2Fblog%2Fwp-content%2Fuploads%2F2013%2F07%2FPetal-Ledger-Round-Menu-Wedding-Place-Setting.jpg&imgrefurl=http%3A%2F%2Fwww.dellivanestudio.example%2Fblog%2Finspiration%2Fsimply-lovely-wedding-menu-place-settings%2F&h=815&w=600&tbnid=8kRqzp_4LUTWEN%3A&zoom=1&docid=72HJKs9PqMxaTN&ei=QwERtYu8LpMsoBF2xdDTRk&tbm=isch&ved=0DHtRNzhKNBk&iact=rc&uact=3&dur=526&page=1&start=0&ndsp=30

https://thumbs3.pixorvane.example/images?q=tbn:QWe7KpLmNvBxRtYu2Hs4DfGhJkZxCvBnMqWeRtYuIoPaSdFgHjK

https://thumbs3.pixorvane.example/images?q=tbn:ZxC8vBnMqW_e42RT_yUioPaSdFgHjKlZxCv66BnM7q_WERtyUiOp

https://thumbs2.pixorvane.example/images?q=tbn:LkJh5GfDsAp9OiUyTrEwQ-MNbV8cXzL3KjHgFdsaPoIuYtReW0Q

Industry/Entity Type

Wedding

```html
<!DOCTYPE html>
<html lang="en">
<head>
<meta charset="utf-8">
<title>Wedding Menu</title>
<link rel="stylesheet" href="https://fonts.googleapis.com/css2?family=Caveat:wght@400;500&family=Source+Sans+3:wght@400;500&display=swap">
<style>
  :root {
    --page: #ffffff;
    --sand: #c6ad97;
    --cocoa: #55382f;
    --cream: #f3e2d1;
  }
  html, body {
    margin: 0;
    padding: 0;
    width: 1200px;
    height: 1000px;
    overflow: hidden;
    background: var(--page);
  }
  .canvas {
    position: relative;
    width: 1200px;
    height: 1000px;
  }
  .menu-disc {
    position: absolute;
    left: 243px;
    top: 135px;
    width: 730px;
    height: 730px;
    border-radius: 50%;
    background: var(--sand);
  }
  .ornament {
    position: absolute;
    background: radial-gradient(ellipse at center, rgba(243,226,209,0.75) 0%, rgba(243,226,209,0.35) 55%, rgba(243,226,209,0) 75%);
  }
  .ornament--top { left: 420px; top: 148px; width: 375px; height: 132px; }
  .ornament--bottom { left: 505px; top: 776px; width: 204px; height: 64px; }
  .line {
    position: absolute;
    left: 243px;
    width: 730px;
    text-align: center;
    color: var(--cocoa);
    white-space: nowrap;
  }
  .title {
    font-family: "Caveat", cursive;
    font-weight: 500;
    font-size: 78px;
    line-height: 1;
    top: 248px;
  }
  .course {
    font-family: "Caveat", cursive;
    font-size: 40px;
    line-height: 1;
  }
  .item {
    font-family: "Source Sans 3", sans-serif;
    font-size: 15px;
    letter-spacing: 0.2px;
    text-transform: uppercase;
    line-height: 20px;
  }
  .dish-label {
    font-family: "Caveat", cursive;
    font-size: 34px;
    text-transform: none;
    vertical-align: -3px;
    letter-spacing: 0;
  }
</style>
</head>
<body>
<div class="canvas">
  <div class="menu-disc"></div>
  <div class="ornament ornament--top" role="img" aria-label="Cream flourish ornament with mirrored swirls"></div>

  <div class="line title">Menu</div>

  <div class="line course" style="top:328px">Salad</div>
  <div class="line item" style="top:373px">Grilled Watermelon &amp; Fig Salad:</div>
  <div class="line item" style="top:399px">Gem Lettuces, Watermelon, Figs, Toasted Hazelnuts,</div>
  <div class="line item" style="top:424px">Balsamic Reduction, Honey-Orange Dressing</div>

  <div class="line course" style="top:450px">Entrée</div>
  <div class="line item" style="top:499px"><span class="dish-label">Beef</span> – Roasted Filet Mignon, Wild Mushrooms, Garlic Mashed Potatoes,</div>
  <div class="line item" style="top:525px">Asparagus with Red Wine Sauce</div>
  <div class="line item" style="top:555px"><span class="dish-label">Fish</span> – Porcini Crusted Halibut, Lemon-Herb Potatoes, Black Kale,</div>
  <div class="line item" style="top:581px">Early Girl Tomatoes</div>
  <div class="line item" style="top:612px"><span class="dish-label">Veggie</span> – Artichoke Agnolotti, Wild Mushrooms, Baby Arugula,</div>
  <div class="line item" style="top:638px">Goat Cheese, White Wine Sauce, Micro Herbs</div>

  <div class="line course" style="top:664px">Wedding Cake</div>
  <div class="line item" style="top:714px">Delicate Butter Pecan</div>
  <div class="line item" style="top:740px">with Fresh Raspberry Mouse</div>

  <div class="ornament ornament--bottom" role="img" aria-label="Small cream flourish ornament"></div>
</div>
</body>
</html>
```